Redesign of 3-4 page site for professional services firm

Our site is www.kestrelvaleadvisors.com. We currently have a simple page made with HostPlumo tools. But the tools are not able to generate the look and feel we desire. We need a home page similar to current that tells a little about our company, our experience and our team. We need a second page to show details of current and past transactions we have assisted our clients with. Currently this page reads like a word document but we would like for it to present in a cleaner fashion and liven it up with some images that link to the industry served. For example, a motorcycle outline in a circle for the powersports related transactions. We would like page to introduce each member of "Our Team" and highlight their experience with a photo of each person. If there is no photo available, we would like a placeholder to be their initials in a circle that can be updated later. We would also like a contact us section whether this is a different page or part of the home page.

Target Market(s)

Retirement minded business owners

Industry/Entity Type

Professional Services

Coding

Coded - Design and coding required

Requirements
Must have
• See project description. Must include a page or section for "Current Listings" and "Recently Completed Transactions" (can be same page)

```html
<!DOCTYPE html>
<html lang="en">
<head>
<meta charset="utf-8">
<title>Kestrel Vale Advisors</title>
<link href="https://fonts.googleapis.com/css2?family=Poppins:wght@300;400;500;600;700&display=swap" rel="stylesheet">
<style>
:root{
  --green:#139a05;
  --yellow:#d8df00;
  --red:#ad0000;
  --ink:#222;
  --muted:#555;
  --gray:#ebebeb;
  --pink:#fcefef;
  --border:#b9b9b9;
  --white:#fff;
}
*{margin:0;padding:0;box-sizing:border-box}
html,body{width:1200px;height:4208px;overflow:hidden}
body{font-family:'Poppins',sans-serif;color:var(--ink);background:var(--white)}
.page{position:relative;width:1200px;height:4208px;overflow:hidden}
.abs{position:absolute}
.bg-shapes{position:absolute;left:0;top:0}
.ph{position:absolute}
.btn{position:absolute;display:flex;align-items:center;justify-content:center;background:var(--green);color:#fff;font-size:10.5px;font-weight:500;text-transform:none}
.label{position:absolute;font-size:13px;font-weight:400;display:flex;align-items:center;gap:12px;text-transform:uppercase}
.label::after{content:"";width:64px;height:2px;background:var(--yellow)}
.h2{position:absolute;font-size:29px;font-weight:300;text-transform:uppercase;letter-spacing:.3px;white-space:nowrap}
.h2 b{font-weight:600}
.center{left:0;width:1200px;text-align:center}
.rule{position:absolute;height:3px;background:var(--yellow);width:78px}
.body-text{position:absolute;font-size:11px;line-height:22.5px;color:var(--muted)}

/* header */
.logo{position:absolute;font-size:18px;font-weight:600;color:var(--ink);display:flex;align-items:center;gap:8px}
.logo::before{content:"";width:12px;height:12px;background:var(--green);border-radius:50%}
.nav{position:absolute;top:16px;font-size:11px;font-weight:400;text-transform:uppercase}
.nav.active{color:#e02020}

/* hero */
.hero-copy{position:absolute;left:121px;top:192px;color:#fff}
.hero-copy .label{position:static;color:#fff}
.hero-title{font-size:40px;line-height:53px;font-weight:300;margin-top:10px;letter-spacing:.5px}
.hero-title b{font-weight:600}

/* cards */
.card{position:absolute;background:#fff;border:2px solid var(--border)}
.sale-card{width:305px;height:318px;top:1563px}
.sale-card .photo{position:absolute;left:11px;top:11px;width:279px;height:143px}
.sold{position:absolute;left:11px;top:11px;background:var(--green);color:#fff;font-size:15px;padding:2px 12px}
.sale-card h3{position:absolute;left:11px;top:166px;font-size:14.5px;font-weight:600}
.sale-card .loc{position:absolute;left:11px;top:188px;font-size:12px}
.sale-card p{position:absolute;left:11px;top:212px;width:280px;font-size:10.5px;line-height:17.8px;color:var(--muted)}
.arrow{position:absolute;width:40px;height:40px}

.review{position:absolute;top:2131px;width:225px;height:147px;background:#fff}
.review .avatar{position:absolute;left:26px;top:13px;width:42px;height:42px;border-radius:50%}
.review .stars{position:absolute;left:78px;top:12px;font-size:11px;color:#e5b400;letter-spacing:1px}
.review .who{position:absolute;left:78px;top:33px;font-size:8.5px;font-weight:600}
.review p{position:absolute;left:26px;top:70px;width:185px;font-size:9.8px;line-height:15px;color:#333}

.member{position:absolute;top:2567px;width:225px;height:310px;background:#fff;border:1px solid #eee3c0}
.member.hl{background:var(--yellow)}
.member .photo{position:absolute;left:0;top:0;width:225px;height:214px}
.member h3{position:absolute;left:15px;top:228px;font-size:14px;font-weight:500}
.member p{position:absolute;left:15px;top:253px;width:200px;font-size:9.5px;line-height:15px;color:var(--muted)}
.member.hl p{color:#444}

.exp{position:absolute;top:3124px;width:305px;height:224px;text-align:center}
.exp svg{position:absolute;left:122px;top:26px}
.exp h3{position:absolute;left:0;width:100%;top:106px;font-size:18px;font-weight:500}
.exp p{position:absolute;left:18px;width:265px;top:134px;font-size:11px;line-height:18px;color:var(--muted)}

/* contact */
.form{position:absolute;left:121px;top:3522px;width:434px;height:291px;background:#fff}
.field{position:absolute;border:1px solid #cfcfcf;font-size:9.5px;color:#888;padding:10px 10px}
.contact-copy{position:absolute;left:688px;top:3540px;width:400px;color:#fff}
.contact-copy .h2{position:static;color:#fff;display:flex;align-items:center;gap:12px}
.contact-copy .h2::after{content:"";width:78px;height:2px;background:var(--yellow)}
.contact-copy p{font-size:10.8px;line-height:19px;margin-top:14px;width:390px}
.contact-copy h4{font-size:18px;font-weight:600;margin-top:14px}
.contact-copy .line{font-size:11px;margin-top:10px}

/* footer */
.f-title{position:absolute;top:3936px;font-size:13px;font-weight:600;text-transform:uppercase;letter-spacing:.3px}
.f-link{position:absolute;font-size:11px;color:#333}
.social{position:absolute;top:3996px;width:26px;height:26px;border-radius:50%;border:1.5px solid var(--green)}
</style>
</head>
<body>
<div class="page">

<!-- backgrounds -->
<svg class="bg-shapes" width="1200" height="4208" viewBox="0 0 1200 4208">
  <defs>
    <linearGradient id="heroGrad" x1="0" y1="0" x2="1" y2="0">
      <stop offset="0" stop-color="#3b3a2e"/>
      <stop offset=".45" stop-color="#7a6a55"/>
      <stop offset="1" stop-color="#b8a48a"/>
    </linearGradient>
  </defs>
  <polygon points="0,590 1200,540 1200,560 0,612" fill="var(--yellow)"/>
  <polygon points="0,1000 1200,1000 1200,1453 0,1377" fill="var(--gray)"/>
  <polygon points="0,1935 1200,1976 1200,2000 0,1955" fill="var(--yellow)"/>
  <polygon points="0,1953 1200,2000 1200,2343 0,2343" fill="var(--green)"/>
  <polygon points="0,2343 1200,2343 1200,2931 0,3001" fill="var(--pink)"/>
  <polygon points="0,3405 1200,3454 1200,3480 0,3425" fill="var(--yellow)"/>
  <polygon points="0,3423 1200,3478 1200,3875 0,3875" fill="var(--red)"/>
</svg>

<!-- header -->
<div class="logo" style="left:121px;top:14px">Kestrel Vale</div>
<div class="nav active" style="left:629px">Home</div>
<div class="nav" style="left:691px">About Us</div>
<div class="nav" style="left:776px">Business Listings</div>
<div class="nav" style="left:905px">Our Team</div>
<div class="btn" style="left:985px;top:11px;width:93px;height:25px;font-size:10.5px">CONTACT US</div>

<!-- hero -->
<svg class="ph" style="left:0;top:49px" width="1200" height="543" role="img" aria-label="Photo of business people reviewing documents in an office">
  <polygon points="0,0 1200,0 1200,491 0,543" fill="url(#heroGrad)"/>
  <polygon points="0,0 520,0 420,543 0,543" fill="#000" opacity=".35"/>
</svg>
<div class="hero-copy">
  <div class="label">Welcome</div>
  <div class="hero-title">STRATEGICALLY <b>NAVIGATING</b><br><b>BUSINESS EXITS</b></div>
</div>
<div class="btn" style="left:121px;top:343px;width:126px;height:27px">Get Started Today</div>
<div class="btn" style="left:252px;top:343px;width:126px;height:27px">CONTACT US</div>

<!-- about -->
<div class="label" style="left:121px;top:658px">About Us</div>
<div class="h2" style="left:121px;top:682px">About Our <b>Company</b></div>
<div class="body-text" style="left:121px;top:726px;width:430px">At Kestrel Vale Advisors, our mission is to empower entrepreneurs and business owners by facilitating seamless transactions that lead to mutual success. We understand that selling or acquiring a business can be a complex and emotional journey, which is why our dedicated team of experts is here to guide you every step of the way. With a commitment to integrity, transparency, and unmatched professionalism, we strive to create a positive and rewarding experience for all our clients.</div>
<div class="btn" style="left:121px;top:909px;width:101px;height:28px">Learn More</div>
<div class="ph" role="img" aria-label="Photo of a business team standing before a glass office building" style="left:753px;top:640px;width:325px;height:296px;background:linear-gradient(135deg,#3f7fc0,#1e2c3e 70%)"></div>
<div class="ph" role="img" aria-label="Photo of colleagues meeting at an office desk" style="left:590px;top:696px;width:213px;height:199px;background:linear-gradient(135deg,#8a7054,#2c2a28)"></div>

<!-- current listings -->
<div class="ph" role="img" aria-label="Photo of two people reviewing charts on a laptop" style="left:121px;top:1063px;width:469px;height:257px;background:linear-gradient(120deg,#5a5552,#b9c4d4 60%,#7aa0cc)"></div>
<div class="h2" style="left:637px;top:1078px">Current <b>Business Listings</b></div>
<div class="rule" style="left:637px;top:1122px;width:90px;height:2px"></div>
<div class="abs" style="left:647px;top:1148px;width:199px;height:72px;border:1.5px solid #999"></div>
<svg class="abs" style="left:670px;top:1160px" width="18" height="22" viewBox="0 0 18 22"><path d="M9 1a7 7 0 0 1 7 7c0 5-7 12-7 12S2 13 2 8a7 7 0 0 1 7-7z" fill="none" stroke="var(--green)" stroke-width="1.6"/><circle cx="9" cy="8" r="2.6" fill="none" stroke="var(--green)" stroke-width="1.6"/></svg>
<div class="abs" style="left:701px;top:1158px;font-size:18px;font-weight:600">$1,100,000</div>
<div class="abs" style="left:703px;top:1186px;font-size:8.5px;line-height:10px;color:#444">Powersports Dealership<br>North Texas</div>
<div class="body-text" style="left:647px;top:1229px;width:436px;font-size:10.8px">Well established multi-line dealership with strong net profit. Excellent staff in place. Dealership has a loyal customer base with further growth potential due to rapid community growth. Serious Inquires with proof of funds only.</div>

<!-- recently completed -->
<div class="h2 center" style="top:1481px">Recently Completed <b>Business Sales</b></div>
<div class="rule" style="left:517px;top:1530px;width:166px"></div>
<svg class="arrow" style="left:57px;top:1702px" viewBox="0 0 40 40"><circle cx="20" cy="20" r="19" fill="#fff" stroke="var(--green)" stroke-width="1.5"/><path d="M23 12l-8 8 8 8" fill="none" stroke="var(--green)" stroke-width="1.5"/></svg>
<svg class="arrow" style="left:1100px;top:1702px" viewBox="0 0 40 40"><circle cx="20" cy="20" r="19" fill="#fff" stroke="var(--green)" stroke-width="1.5"/><path d="M17 12l8 8-8 8" fill="none" stroke="var(--green)" stroke-width="1.5"/></svg>

<div class="card sale-card" style="left:121px">
  <div class="photo" role="img" aria-label="Photo of friends bowling at an entertainment venue" style="background:linear-gradient(135deg,#6b8aa8,#3a3a44)"></div>
  <div class="sold">Sold</div>
  <h3>Sports and Entertainment Venue</h3>
  <div class="loc">East Texas</div>
  <p>Once in a generation opportunity to take over exciting sports and entertainment complex. Run by the same family for the past 37 years this is a unique opportunity to acquire a unique and profitable business in an very exciting industry.</p>
</div>
<div class="card sale-card" style="left:446px">
  <div class="photo" role="img" aria-label="Photo of a dealership staff member talking with a customer" style="background:linear-gradient(135deg,#d9d4cc,#5b5650)"></div>
  <div class="sold">Sold</div>
  <h3>Powersports Dealership</h3>
  <div class="loc">North Texas</div>
  <p>Multi-line metric dealership experiencing tremendous growth with even more potential due to rapid growth in surrounding areas. Dealership represents six lines and is a great opportunity for the right owner/operator.</p>
</div>
<div class="card sale-card" style="left:771px">
  <div class="photo" role="img" aria-label="Photo of hands working on accounts with a calculator and pen" style="background:linear-gradient(135deg,#e8ecf1,#9aa6b4)"></div>
  <div class="sold">Sold</div>
  <h3>Bookkeeping and Tax Practice</h3>
  <div class="loc">Southern California</div>
  <p>This firm specializes in providing remote and virtual tax and bookkeeping services which keeps overhead low and profits high. Clients consist of individuals and small to medium sized businesses.</p>
</div>

<!-- reviews -->
<div class="h2 center" style="top:2050px;color:#fff;font-weight:600">Reviews</div>
<div class="review" style="left:121px">
  <div class="avatar" role="img" aria-label="Reviewer portrait" style="background:linear-gradient(#d8c2a8,#3b4a66)"></div>
  <div class="stars">★★★★★</div><div class="who">Owen Mercer</div>
  <p>"Lorem ipsum dolor sit amet, consectetur adipiscing elit. Pellentesque at tortor purus. Nulla facilisi. Praesent eget gravida leo.</p>
</div>
<div class="review" style="left:365px">
  <div class="avatar" role="img" aria-label="Reviewer portrait" style="background:linear-gradient(#e0cbb5,#3a3430)"></div>
  <div class="stars">★★★★★</div><div class="who">Lena Hartwell</div>
  <p>"Lorem ipsum dolor sit amet, consectetur adipiscing elit. Pellentesque at tortor purus. Nulla facilisi. Praesent eget gravida leo.</p>
</div>
<div class="review" style="left:609px">
  <div class="avatar" role="img" aria-label="Reviewer portrait" style="background:linear-gradient(#c49a7a,#5a3a28)"></div>
  <div class="stars">★★★★★</div><div class="who">Caleb Rowe</div>
  <p>"Lorem ipsum dolor sit amet, consectetur adipiscing elit. Pellentesque at tortor purus. Nulla facilisi. Praesent eget gravida leo.</p>
</div>
<div class="review" style="left:853px">
  <div class="avatar" role="img" aria-label="Reviewer portrait" style="background:linear-gradient(#e8a070,#c4632e)"></div>
  <div class="stars">★★★★★</div><div class="who">Nora Vance</div>
  <p>"Lorem ipsum dolor sit amet, consectetur adipiscing elit. Pellentesque at tortor purus. Nulla facilisi. Praesent eget gravida leo.</p>
</div>

<!-- team -->
<div class="h2 center" style="top:2396px">Our <b>Team</b></div>
<div class="body-text" style="left:278px;top:2458px;width:644px;text-align:center;font-size:11px;color:#444">Together, our team of CPAs, attorneys, real estate brokers, and financial advisors work collaboratively to provide you with a holistic approach to business transactions. With our combined knowledge and experience, we strive to ensure a smooth and successful journey for our clients, delivering exceptional results and peace of mind.</div>
<div class="member" style="left:121px">
  <div class="photo" role="img" aria-label="Portrait of Daniel Whitfield" style="background:linear-gradient(#ffffff 40%,#c9a88c 40%,#1f2633)"></div>
  <h3>Daniel Whitfield, CPA, JD</h3>
  <p>Daniel is a forward thinking Certified Public Accountant and JD, blending business, finance and legal expertise...</p>
</div>
<div class="member hl" style="left:365px">
  <div class="photo" role="img" aria-label="Portrait of Reed Calloway" style="background:linear-gradient(#ffffff 40%,#d0ad92 40%,#2a2a2a)"></div>
  <h3>Reed Calloway</h3>
  <p>Reed has more than 30 years of experience within the financial and insurance services fields...</p>
</div>
<div class="member" style="left:609px">
  <div class="photo" role="img" aria-label="Portrait of Miles Brenner" style="background:linear-gradient(#ffffff 40%,#d4a98a 40%,#2e3540)"></div>
  <h3>Miles Brenner</h3>
  <p>Miles is a sales and marketing expert in the powersports and automotive industries with a clientele that has...</p>
</div>
<div class="member" style="left:853px">
  <div class="photo" role="img" aria-label="Portrait of Walter Ashby" style="background:linear-gradient(#ffffff 40%,#e0b8a0 40%,#2b3a55)"></div>
  <h3>Walter Ashby</h3>
  <p>Walter is a truly seasoned professional with 40+ years experience as a licensed broker &amp; executive...</p>
</div>

<!-- experience -->
<div class="h2 center" style="top:3022px">Our <b>Experience</b></div>
<div class="rule" style="left:561px;top:3071px"></div>
<svg class="arrow" style="left:57px;top:3216px" viewBox="0 0 40 40"><circle cx="20" cy="20" r="19" fill="#fff" stroke="var(--green)" stroke-width="1.5"/><path d="M23 12l-8 8 8 8" fill="none" stroke="var(--green)" stroke-width="1.5"/></svg>
<svg class="arrow" style="left:1100px;top:3216px" viewBox="0 0 40 40"><circle cx="20" cy="20" r="19" fill="#fff" stroke="var(--green)" stroke-width="1.5"/><path d="M17 12l8 8-8 8" fill="none" stroke="var(--green)" stroke-width="1.5"/></svg>

<div class="card exp" style="left:121px">
  <svg width="58" height="58" viewBox="0 0 58 58"><circle cx="29" cy="29" r="26" fill="none" stroke="var(--green)" stroke-width="2"/><circle cx="29" cy="29" r="15" fill="none" stroke="var(--green)" stroke-width="2" stroke-dasharray="5 3"/><circle cx="29" cy="29" r="7" fill="none" stroke="var(--green)" stroke-width="2"/></svg>
  <h3>Experience</h3>
  <p>With decades of experience Kestrel Vale Advisors has proudly assisted numerous clients in successfully navigating the intricate journey of selling their businesses.</p>
</div>
<div class="card exp" style="left:446px">
  <svg width="58" height="58" viewBox="0 0 58 58"><circle cx="29" cy="10" r="7" fill="none" stroke="var(--green)" stroke-width="2"/><circle cx="10" cy="44" r="7" fill="none" stroke="var(--green)" stroke-width="2"/><circle cx="48" cy="44" r="7" fill="none" stroke="var(--green)" stroke-width="2"/><circle cx="29" cy="32" r="8" fill="none" stroke="var(--green)" stroke-width="2"/><path d="M29 17v7M16 40l7-4M42 40l-7-4" stroke="var(--green)" stroke-width="2"/></svg>
  <h3>Knowledge</h3>
  <p>Our team brings a wealth of knowledge and expertise acquired through years of working closely with entrepreneurs and business owners across diverse industries.</p>
</div>
<div class="card exp" style="left:771px">
  <svg width="58" height="58" viewBox="0 0 58 58"><circle cx="29" cy="29" r="26" fill="none" stroke="var(--green)" stroke-width="2" stroke-dasharray="30 6"/><path d="M29 16a9 9 0 0 1 5 16v5h-10v-5a9 9 0 0 1 5-16z" fill="none" stroke="var(--green)" stroke-width="2"/><path d="M25 41h8" stroke="var(--green)" stroke-width="2"/></svg>
  <h3>Unique challenges</h3>
  <p>We understand the unique challenges and complexities involved in selling a business, from valuation and marketing to negotiations and closing the deal.</p>
</div>

<!-- contact -->
<div class="form">
  <div class="field" style="left:26px;top:28px;width:181px;height:36px">First name</div>
  <div class="field" style="left:227px;top:28px;width:181px;height:36px">Last name</div>
  <div class="field" style="left:26px;top:84px;width:181px;height:36px">Email</div>
  <div class="field" style="left:227px;top:84px;width:181px;height:36px">Phone number</div>
  <div class="field" style="left:26px;top:136px;width:382px;height:82px">Message</div>
  <div class="btn" style="left:26px;top:239px;width:382px;height:28px">SUBMIT</div>
</div>
<div class="contact-copy">
  <div class="h2">Contact <b style="font-weight:500">Us</b></div>
  <p>We strive to stay in communication with our clients. Have a question about how we can match your specific needs? Send us a message, or give us a call. We're always happy to meet new customers!</p>
  <h4>Kestrel Vale Advisors</h4>
  <div class="line">218 Larkspur Road, Fairview, Oklahoma 74102, United States</div>
  <div class="line" style="margin-top:14px">405-555-0148</div>
</div>
<div class="btn" style="left:688px;top:3762px;width:145px;height:28px">GET STARTED TODAY</div>

<!-- footer -->
<div class="logo" style="left:121px;top:3950px;font-size:22px">Kestrel Vale</div>
<div class="social" style="left:122px"></div>
<div class="social" style="left:158px"></div>
<div class="social" style="left:194px"></div>

<div class="f-title" style="left:456px">Quick Links</div>
<div class="f-link" style="left:456px;top:3982px">Home</div>
<div class="f-link" style="left:456px;top:4009px">About us</div>
<div class="f-link" style="left:456px;top:4036px">Business listings</div>
<div class="f-link" style="left:456px;top:4063px">Our team</div>

<div class="f-title" style="left:624px">Contact Info</div>
<svg class="abs" style="left:624px;top:3983px" width="9" height="12" viewBox="0 0 9 12"><path d="M4.5 0.5a4 4 0 0 1 4 4c0 3-4 7-4 7s-4-4-4-7a4 4 0 0 1 4-4z" fill="var(--green)"/></svg>
<div class="f-link" style="left:637px;top:3980px;line-height:15px">218 Larkspur Road, Fairview,<br>Oklahoma 74102, United States</div>
<svg class="abs" style="left:624px;top:4028px" width="10" height="10" viewBox="0 0 10 10"><path d="M2 0.5l2 2.2-1 1.3a6 6 0 0 0 3 3l1.3-1 2.2 2-1.2 1.5C4.5 9.5 0.5 5.5 0.5 1.7z" fill="var(--green)"/></svg>
<div class="f-link" style="left:637px;top:4025px">405-555-0148</div>

<div class="f-title" style="left:867px">Subscribe</div>
<div class="f-link" style="left:867px;top:3980px;line-height:15px;width:200px">Sign up to hear from us about exciting new opportunities.</div>
<div class="abs" style="left:867px;top:4052px;width:137px;height:28px;border:1px solid #999;font-size:9.5px;padding:8px 12px;color:#444">Email</div>
<div class="btn" style="left:1004px;top:4052px;width:74px;height:28px">SIGN UP</div>

<div class="abs" style="left:121px;top:4118px;width:957px;height:1px;background:#999"></div>
<div class="abs" style="left:121px;top:4141px;font-size:9.5px;color:#333">Copyright © 2023 Kestrel Vale Advisors - All Rights Reserved</div>
<div class="abs" style="left:969px;top:4141px;font-size:9.5px;color:#333;width:109px;text-align:right">Powered by <span style="color:var(--green)">HostPlumo</span></div>

</div>
</body>
</html>
```